Dental Practice Billboard Design

We are a newer dental practice in need of a simple but appealing billboard for our growing dental practice to attract new patients. The practice is owned by husband and wife dentists and is family friendly in a small town in Kentucky. We try to be very friendly and caring to our patients. Would prefer a blue background for the billboard and our tooth logo to be prominent. We are partial to the Patua One font used in the image below but please feel free to tweak it as you deem necessary. The shape of the uppercase D and lowercase g are why we like that font, so fonts with a similarly shaped “D” and “g” would work as well. Please include our phone number (606) 847-3962. Please see our website Harlowfamilydentistry.com for more info on the practice if needed. Thank you! Looking forward to seeing your creation.
Updates

The dimensions will be 12ft x 24ft (3.6576m x 7.3152m). Apologies for not including this in the original prompt. Thank you all for your submissions.

Industry/Entity Type

Dental

Font styles to use
Other font styles liked:
• Patua One

Colors
0054AA
0677BA
7BADD7
CADEEF
E8F1F8
0094D4
00A9DD
6FCCEA
C7EBF8
E9F6FB
00AB8E
00BBA5
67D7C9
C6EFE9
E9F9F6
59FF00
82FF00
B8FF75
E3FFCB
F4FFEA

Requirements
Must have
• Phone number, website, Logo, Practice name “Harlow Family Dentistry”
Should not have
• A tagline or slogan

```html
<!DOCTYPE html>
<html lang="en">
<head>
<meta charset="utf-8">
<title>Harlow Family Dentistry Billboard</title>
<link href="https://fonts.googleapis.com/css2?family=Bree+Serif&display=swap" rel="stylesheet">
<style>
  :root {
    --page-bg: #ececec;
    --brand-blue: #0054aa;
    --deep-blue: #1f4fa6;
    --mid-blue: #0677ba;
    --teal: #00ab8e;
    --teal-soft: #c6efe9;
    --green: #2fb34a;
    --white: #ffffff;
    --photo-dark: #1b2f6e;
    --photo-mid: #2c57a8;
  }
  * { margin: 0; padding: 0; box-sizing: border-box; }
  html, body { width: 1200px; height: 1200px; overflow: hidden; }
  body {
    background: var(--page-bg);
    font-family: "Bree Serif", Georgia, serif;
    position: relative;
  }
  .billboard {
    position: absolute;
    left: 85px;
    top: 408px;
    width: 1030px;
    height: 385px;
    overflow: hidden;
    background: var(--white);
  }
  .billboard-art,
  .hero-photo {
    position: absolute;
    inset: 0;
    width: 1030px;
    height: 385px;
  }
  .phone-tab {
    position: absolute;
    left: 40px;
    top: 0;
    width: 98px;
    height: 118px;
    background: var(--green);
    border-bottom-left-radius: 34px;
  }
  .phone-icon {
    position: absolute;
    left: 56px;
    top: 46px;
    width: 68px;
    height: 68px;
  }
  .phone-number {
    position: absolute;
    left: 147px;
    top: 56px;
    font-size: 38px;
    line-height: 48px;
    color: var(--white);
    letter-spacing: 0.5px;
  }
  .website {
    position: absolute;
    left: 56px;
    top: 330px;
    font-size: 20px;
    line-height: 28px;
    color: var(--white);
  }
  .practice-name {
    position: absolute;
    left: 718px;
    top: 52px;
    display: flex;
    align-items: center;
    gap: 14px;
    color: var(--brand-blue);
  }
  .name-mark {
    width: 54px;
    height: 54px;
    border-radius: 50%;
    background: var(--brand-blue);
    flex: none;
  }
  .name-lines { display: flex; flex-direction: column; }
  .name-primary { font-size: 42px; line-height: 44px; }
  .name-secondary { font-size: 22px; line-height: 26px; }
</style>
</head>
<body>
  <section class="billboard">
    <svg class="billboard-art" viewBox="0 0 1030 385" aria-hidden="true">
      <defs>
        <linearGradient id="panelGradient" x1="0" y1="0" x2="0.35" y2="1">
          <stop offset="0" stop-color="#1f5cb0"/>
          <stop offset="0.6" stop-color="#1468b0"/>
          <stop offset="1" stop-color="#11a08c"/>
        </linearGradient>
        <linearGradient id="cornerGradient" x1="0" y1="0" x2="1" y2="1">
          <stop offset="0" stop-color="#b6e2da"/>
          <stop offset="1" stop-color="#f3fbf9"/>
        </linearGradient>
      </defs>
      <path d="M0 0 H620 C720 70 775 210 784 385 H0 Z" fill="url(#panelGradient)"/>
      <path d="M784 385 C820 300 900 262 1030 256 V385 Z" fill="url(#cornerGradient)"/>
    </svg>

    <svg class="hero-photo" viewBox="0 0 1030 385" role="img" aria-label="Photo of a young patient in safety goggles having a dental check-up">
      <defs>
        <linearGradient id="photoGradient" x1="0" y1="0" x2="1" y2="0.6">
          <stop offset="0" stop-color="#2f66b6"/>
          <stop offset="0.55" stop-color="var(--photo-mid)"/>
          <stop offset="1" stop-color="var(--photo-dark)"/>
        </linearGradient>
      </defs>
      <path d="M150 0 H590 C700 60 770 200 784 385 H440 C270 335 165 190 150 0 Z" fill="url(#photoGradient)" opacity="0.95"/>
    </svg>

    <div class="phone-tab"></div>
    <svg class="phone-icon" viewBox="0 0 68 68" aria-hidden="true">
      <circle cx="34" cy="34" r="30" fill="none" stroke="#ffffff" stroke-width="4"/>
      <path d="M24 18 L30 18 L32 27 L28 30 C30 36 33 39 38 41 L41 37 L50 39 L50 45 C50 48 47 50 44 50 C30 49 19 38 18 24 C18 21 21 18 24 18 Z" fill="#ffffff"/>
      <path d="M38 20 A12 12 0 0 1 48 30" fill="none" stroke="#ffffff" stroke-width="3" stroke-linecap="round"/>
      <path d="M37 27 A5 5 0 0 1 41 31" fill="none" stroke="#ffffff" stroke-width="3" stroke-linecap="round"/>
    </svg>
    <p class="phone-number">(606) 847-3962</p>
    <p class="website">Harlowfamilydentistry.com</p>

    <div class="practice-name">
      <span class="name-mark"></span>
      <div class="name-lines">
        <span class="name-primary">Harlow</span>
        <span class="name-secondary">Family Dentistry</span>
      </div>
    </div>
  </section>
</body>
</html>
```